Business Cards/Stationary/Letterhead for Crestline Weight Loss Center
Be Healthy, Be Fit, and Be Ready to Lose Weight!
Creative Brief
Simple
Derek Tolsan, PA
Physician Assistant, Co-founder
52816 Birchwood Lane Fremont, CA 94592-7731
CrestlineSlim@mailhaven.example
www.crestlineslim.example
Aim for Results with Crestline Weight Loss! HCG, Appetite Suppressants,B12/B-Complex injections, Menu Plans, Exercise Plans, Nutriceuticals, Supplements.
Present this card to a friend; If your friend signs up, you will receive a 20% discount. The referrals are endless. If you refer 5 friends who sign up then you will receive 100% discount on your next visit. Just make sure your friend puts your name down in the "referral" section of the information sheet and you will be that much closer to saving. (Discount will only apply to weight loss program, discount only applicable for one month or week supply of medication. Non-transferrable. Referral cannot be an existing patient.) Appointment Date: _________ Time: _____

```html
<!DOCTYPE html>
<html lang="en">
<head>
<meta charset="utf-8">
<title>Crestline Weight Loss Center – Stationery</title>
<link rel="stylesheet" href="https://fonts.googleapis.com/css2?family=Lato:wght@400;700&family=Cinzel:wght@400&display=swap">
<style>
  :root {
    --green: #8dbb25;
    --green-dark: #6f9a15;
    --orange: #e27812;
    --paper: #ffffff;
    --paper-shade: #eeeeea;
    --ink: #5a5a5a;
    --backdrop: #ece6dc;
    --caption: #6d655a;
  }
  * { margin: 0; padding: 0; box-sizing: border-box; }
  html, body { width: 1200px; height: 600px; overflow: hidden; }
  body { background: var(--backdrop); font-family: "Lato", sans-serif; color: var(--ink); }
  .canvas { position: relative; width: 1200px; height: 600px; }
  .piece { position: absolute; background: var(--paper); box-shadow: 0 2px 6px rgba(0,0,0,.18); overflow: hidden; }
  .piece svg.wave { position: absolute; left: 0; bottom: 0; width: 100%; }
  .brand { display: flex; align-items: center; gap: 5px; position: absolute; }
  .brand-dot { border-radius: 50%; background: var(--orange); flex: none; }
  .brand-name { color: var(--green); font-weight: 700; white-space: nowrap; }
  .caption { position: absolute; font-family: "Cinzel", serif; font-size: 9px; letter-spacing: 1.5px; color: var(--caption); text-align: center; }

  /* business card front */
  .card-front { left: 24px; top: 245px; width: 144px; height: 98px; }
  .card-front .brand { left: 8px; top: 9px; }
  .card-front .brand-dot { width: 9px; height: 9px; }
  .card-front .brand-name { font-size: 7.5px; }
  .card-front .card-contact { position: absolute; right: 8px; top: 22px; text-align: right; color: var(--ink); font-size: 4.4px; line-height: 5.6px; }
  .card-front .card-contact strong { font-size: 5.5px; color: var(--green-dark); }

  /* business card back */
  .card-back { left: 24px; top: 372px; width: 144px; height: 100px; }
  .card-back .referral { position: absolute; left: 9px; right: 9px; top: 12px; font-size: 5px; line-height: 7px; }
  .card-back .appointment { position: absolute; left: 9px; top: 64px; font-size: 5px; color: var(--green-dark); font-weight: 700; }

  /* letterhead */
  .letterhead { left: 221px; top: 24px; width: 283px; height: 523px; }
  .letterhead .brand { left: 20px; top: 22px; }
  .letterhead .brand-dot { width: 14px; height: 14px; }
  .letterhead .brand-name { font-size: 10px; }
  .letterhead .letter-contact { position: absolute; left: 20px; bottom: 18px; color: #fff; font-size: 5.5px; line-height: 8px; }

  /* envelopes */
  .envelope { position: absolute; }
  .envelope svg { display: block; width: 100%; height: 100%; }
  .env-green { left: 653px; top: 24px; width: 475px; height: 180px; }
  .env-orange { left: 677px; top: 132px; width: 475px; height: 175px; }
  .env-white { left: 701px; top: 240px; width: 451px; height: 168px; }
  .env-white .seal { position: absolute; left: 50%; top: 88px; transform: translateX(-50%); }
  .env-white .brand-dot { width: 12px; height: 12px; }
  .env-front { left: 653px; top: 408px; width: 499px; height: 156px; }
  .env-front .brand { left: 18px; top: 18px; }
  .env-front .brand-dot { width: 12px; height: 12px; }
  .env-front .brand-name { font-size: 9px; }
  .env-front .return-address { position: absolute; left: 18px; top: 38px; font-size: 5px; color: var(--green-dark); }
</style>
</head>
<body>
<main class="canvas">

  <!-- business card front -->
  <section class="piece card-front">
    <svg class="wave" viewBox="0 0 144 36" height="36" preserveAspectRatio="none" aria-hidden="true">
      <path d="M0 12 C40 2 90 20 144 6 L144 36 L0 36Z" fill="var(--green)"/>
      <path d="M0 12 C40 2 90 20 144 6" fill="none" stroke="var(--orange)" stroke-width="2.5"/>
      <path d="M0 17 C45 8 95 24 144 11" fill="none" stroke="#fff" stroke-width="1"/>
    </svg>
    <div class="brand"><span class="brand-dot"></span><span class="brand-name">Crestline Weight Loss Center</span></div>
    <div class="card-contact">
      <strong>Derek Tolsan, PA</strong><br>
      Physician Assistant, Co-founder<br>
      52816 Birchwood Lane<br>
      Fremont, CA 94592-7731<br>
      CrestlineSlim@mailhaven.example<br>
      www.crestlineslim.example
    </div>
  </section>

  <!-- business card back -->
  <section class="piece card-back">
    <svg class="wave" viewBox="0 0 144 20" height="20" preserveAspectRatio="none" aria-hidden="true">
      <path d="M0 10 C40 0 90 18 144 6 L144 20 L0 20Z" fill="var(--green)"/>
      <path d="M0 10 C40 0 90 18 144 6" fill="none" stroke="var(--orange)" stroke-width="1.5"/>
    </svg>
    <p class="referral">Present this card to a friend; If your friend signs up, you will receive a 20% discount. The referrals are endless.</p>
    <p class="appointment">Appointment Date: ________ Time: _____</p>
  </section>
  <div class="caption" style="left:24px; top:482px; width:144px;">Business Card Back</div>

  <!-- letterhead -->
  <section class="piece letterhead">
    <div class="brand"><span class="brand-dot"></span><span class="brand-name">Crestline Weight Loss Center</span></div>
    <svg class="wave" viewBox="0 0 283 110" height="110" preserveAspectRatio="none" aria-hidden="true">
      <path d="M0 52 C80 20 170 70 283 30 L283 110 L0 110Z" fill="var(--green)"/>
      <path d="M0 36 C90 6 170 58 283 18" fill="none" stroke="var(--orange)" stroke-width="5"/>
      <path d="M0 46 C85 14 170 64 283 26" fill="none" stroke="var(--green)" stroke-width="2"/>
      <path d="M0 58 C85 28 175 76 283 38" fill="none" stroke="#fff" stroke-width="1.2"/>
    </svg>
    <div class="letter-contact">
      52816 Birchwood Lane Fremont, CA 94592-7731<br>
      CrestlineSlim@mailhaven.example<br>
      www.crestlineslim.example
    </div>
  </section>
  <div class="caption" style="left:221px; top:571px; width:283px;">Letter-head Option 1</div>

  <!-- envelope backs -->
  <div class="envelope env-green" aria-hidden="true">
    <svg viewBox="0 0 475 180" preserveAspectRatio="none">
      <rect width="475" height="180" fill="var(--paper-shade)"/>
      <path d="M0 0 H475 V60 L237 100 L0 60Z" fill="var(--green)"/>
    </svg>
  </div>
  <div class="envelope env-orange" aria-hidden="true">
    <svg viewBox="0 0 475 175" preserveAspectRatio="none">
      <rect width="475" height="175" fill="var(--paper-shade)"/>
      <path d="M0 0 H475 V56 L237 96 L0 56Z" fill="var(--orange)"/>
    </svg>
  </div>
  <div class="envelope env-white">
    <svg viewBox="0 0 451 168" preserveAspectRatio="none" aria-hidden="true">
      <rect width="451" height="168" fill="var(--paper)"/>
      <path d="M0 0 H451 V52 L225 90 L0 52Z" fill="#f7f7f4" stroke="#dcdcd6" stroke-width="1"/>
    </svg>
    <div class="brand seal"><span class="brand-dot"></span></div>
  </div>

  <!-- envelope front -->
  <section class="piece env-front">
    <div class="brand"><span class="brand-dot"></span><span class="brand-name">Crestline Weight Loss Center</span></div>
    <p class="return-address">52816 Birchwood Lane Fremont, CA 94592-7731</p>
  </section>
  <div class="caption" style="left:653px; top:576px; width:499px;">Envelope Option 2</div>

</main>
</body>
</html>
```